VORALUX SYSTEMS BUSINESS CARD DESIGN

WE WANT COMPLETE NEW DESIGN OF OUR BUSINESS CARD. WE ARE AN INTEGRATION COMPANY, WHERE WE INTEGRATE IOT/SMART SYSTEMS TO HOMES AND CORPORATE CUSTOMERS. WE SUPPLY AND INSTALL AUTOMATION PRODUCTS. THE FINAL DESIGN SHOULD COMMUNICATE TECHNOLOGY. THE CARD DESIGN SHOULD BE VERY IMPACT FULL. LOGO NEEDS TO BE THERE. IT WOULD NICE IF THE DESIGN WAS CLEAN. COLORS IS UP TO DESIGNER TO PLAY WITH, OR CAN STICK TO CORPORATE COLORS (FOLLOW LOGO). I HAVE ADDED FEW REFERENCE PHOTOS TO DRAW INSPIRATION MAYBE. I HAVE ADDED A HEX DESIGN, ITS NOT NECESSARY TO USE THIS DESIGN, ITS UPTO DESIGNER, JUST ADDED IF NEEDED TO PLAY WITH DESIGN.

Target Market(s)

Private end users and corporate clients

Industry/Entity Type

technology, home automation, home theaters, building management systems, IOT

Contact Information for Business Card

It should include Employee name, personal number, office number, email address, both in English and arabic. DETAILS TO INCLUDE :DANIEL MARUVEN, MOBILE 0097150738219,OFFCIE 009714368174, DANIEL@VORALUXSYS.CO

Requirements
Must have
• Should feel like a technology company from design. Details both and in English and arabic (or at least have provision for arabic in design).
Nice to have
• I would like logo on one side, and details on the other side. Logo design side should communicate technology with logo. Other side can be clean just with information or also have some design aspects following from logo side. it would be interesting to see submissions with square design as well (that looks like an app Icon). colors could be of logo, red black grey and white. I have added some designs to draw inspiration from

```html
<!DOCTYPE html>
<html lang="en">
<head>
<meta charset="utf-8">
<title>Voralux Systems – Business Card</title>
<link rel="stylesheet" href="https://fonts.googleapis.com/css2?family=Poppins:wght@300;400;600;800&family=Michroma&family=Cairo:wght@400;700&display=swap">
<style>
  :root {
    --backdrop: #3a2a2c;
    --card-light: #c9c9c9;
    --card-mid: #a9a9a9;
    --card-dark: #8d8d8d;
    --ink: #1d1d1f;
    --brand-red: #e3141f;
    --dot-blue: #1a6fe0;
    --dot-green: #0e9a5a;
    --dot-yellow: #f5b511;
    --dot-pink: #ee3a62;
  }
  * { margin: 0; padding: 0; box-sizing: border-box; }
  html, body {
    width: 1200px; height: 800px; overflow: hidden;
    background: var(--backdrop);
  }
  .stage {
    width: 1200px; height: 800px;
    display: flex; align-items: center; justify-content: center; gap: 48px;
  }
  .card {
    position: relative;
    width: 540px; height: 310px;
    border-radius: 18px;
    background: linear-gradient(135deg, var(--card-light) 0%, var(--card-mid) 55%, var(--card-dark) 100%);
    box-shadow: 0 18px 40px rgba(0,0,0,.45), inset 0 0 0 2px rgba(255,255,255,.35);
    overflow: hidden;
  }

  /* Brand name block */
  .brand { display: flex; align-items: center; gap: 12px; }
  .brand-dot {
    width: 30px; height: 30px; border-radius: 50%;
    background: var(--brand-red);
  }
  .brand-name {
    font-family: "Poppins", sans-serif;
    font-weight: 800;
    color: var(--ink);
    letter-spacing: 1px;
    line-height: 1;
  }
  .tagline {
    font-family: "Michroma", sans-serif;
    color: var(--ink);
    letter-spacing: 3px;
  }

  /* Front */
  .card-front .brand { position: absolute; left: 44px; top: 56px; }
  .card-front .brand-name { font-size: 34px; }
  .card-front .tagline { position: absolute; left: 44px; top: 112px; font-size: 12px; }
  .network-field {
    position: absolute; right: 0; bottom: 0;
    width: 380px; height: 190px;
    background:
      radial-gradient(circle at 30% 60%, rgba(26,111,224,.28), transparent 45%),
      radial-gradient(circle at 70% 40%, rgba(245,181,17,.28), transparent 45%),
      radial-gradient(circle at 55% 85%, rgba(238,58,98,.22), transparent 40%),
      radial-gradient(circle at 85% 80%, rgba(14,154,90,.25), transparent 40%);
  }

  /* Back */
  .person { position: absolute; left: 40px; top: 44px; }
  .person-name {
    font-family: "Poppins", sans-serif;
    font-weight: 800;
    font-size: 30px;
    color: var(--brand-red);
    letter-spacing: .5px;
    line-height: 1.1;
  }
  .person-name-ar {
    font-family: "Cairo", sans-serif;
    font-weight: 700; font-size: 18px;
    color: var(--brand-red);
    direction: rtl;
  }
  .person-role {
    font-family: "Poppins", sans-serif;
    font-weight: 300; font-size: 14px;
    color: var(--ink);
    display: flex; gap: 10px; align-items: baseline;
  }
  .person-role .ar { font-family: "Cairo", sans-serif; font-weight: 400; }

  .contact-list {
    position: absolute; left: 40px; bottom: 36px;
    list-style: none;
    font-family: "Poppins", sans-serif; font-size: 13px; color: var(--ink);
  }
  .contact-list li { display: flex; align-items: center; gap: 10px; margin-top: 7px; }
  .contact-list .label-ar { font-family: "Cairo", sans-serif; font-size: 12px; }
  .contact-list svg { width: 14px; height: 14px; fill: none; stroke: var(--brand-red); stroke-width: 2; }

  .card-back .brand { position: absolute; right: 32px; top: 150px; gap: 8px; }
  .card-back .brand-dot { width: 18px; height: 18px; }
  .card-back .brand-name { font-size: 20px; }
  .card-back .tagline { position: absolute; right: 32px; top: 180px; font-size: 7px; letter-spacing: 2px; }
</style>
</head>
<body>
<main class="stage">

  <section class="card card-front" aria-label="Business card, brand side">
    <div class="brand">
      <span class="brand-dot"></span>
      <span class="brand-name">VORALUX SYSTEMS</span>
    </div>
    <p class="tagline">A VORALUX GROUP DIVISION.</p>
    <div class="network-field" role="img" aria-label="Network of coloured nodes joined by thin lines, suggesting connected smart devices"></div>
  </section>

  <section class="card card-back" aria-label="Business card, contact side">
    <div class="person">
      <h1 class="person-name">DANIEL MARUVEN</h1>
      <p class="person-name-ar">دانيال مارفن</p>
      <p class="person-role"><span>General Manager</span><span class="ar">المدير العام</span></p>
    </div>

    <ul class="contact-list">
      <li>
        <svg viewBox="0 0 24 24"><rect x="6" y="2" width="12" height="20" rx="2"/><line x1="11" y1="18" x2="13" y2="18"/></svg>
        <span>0097150738219</span><span class="label-ar">موبايل</span>
      </li>
      <li>
        <svg viewBox="0 0 24 24"><path d="M5 3h4l2 5-3 2a11 11 0 0 0 6 6l2-3 5 2v4a2 2 0 0 1-2 2A17 17 0 0 1 3 5a2 2 0 0 1 2-2z"/></svg>
        <span>009714368174</span><span class="label-ar">مكتب</span>
      </li>
      <li>
        <svg viewBox="0 0 24 24"><rect x="3" y="5" width="18" height="14" rx="2"/><polyline points="3,6 12,13 21,6"/></svg>
        <span>DANIEL@VORALUXSYS.CO</span>
      </li>
    </ul>

    <div class="brand">
      <span class="brand-dot"></span>
      <span class="brand-name">VORALUX SYSTEMS</span>
    </div>
    <p class="tagline">A VORALUX GROUP DIVISION.</p>
  </section>

</main>
</body>
</html>
```